Land Buying Company Needs Letterhead for Direct Mail Marketing to Land Owners

We are looking for a professional letterhead that we will be including in our direct mail marketing. We will be sending this to land owners who may be interested in selling or purchasing land.

The letterhead needs to be editable. Headers and footers would look nice, but we are open. We would want it to include our address, website, phone, and email info. For right now the address to use for design purposes would the following:

Address: 412 Fenwick Avenue #300
Dallas, TX 75319
Website - www.quillbrookacres.com
Email - info@quillbrookacres.com
Phone - 866-492-ACRE

I have attached our logo zip file that we just had done on Pixel Harbor. Let me know what questions you have, and thank you.

```html
<!DOCTYPE html>
<html lang="en">
<head>
<meta charset="utf-8">
<title>Quillbrook Acres – Letterhead Footer</title>
<link rel="stylesheet" href="https://fonts.googleapis.com/css2?family=Carlito&display=swap">
<style>
  :root {
    --paper: #ffffff;
    --ink-grey: #6d6e71;
    --brand-green: #7a9e3e;
    --icon-white: #ffffff;
    --arc-shade: #000000;
  }
  html, body {
    margin: 0;
    padding: 0;
    width: 1200px;
    height: 241px;
    overflow: hidden;
    background: var(--paper);
  }
  .letterhead-footer {
    position: relative;
    width: 1200px;
    height: 241px;
    overflow: hidden;
    background: var(--paper);
  }
  .decor-arcs {
    position: absolute;
    inset: 0;
  }
  .contact-list {
    position: absolute;
    left: 0;
    top: 0;
    margin: 0;
    padding: 0;
    list-style: none;
    font-family: "Carlito", "Calibri", sans-serif;
    font-size: 16.5px;
    color: var(--ink-grey);
  }
  .contact-item {
    position: absolute;
    left: 0;
    display: flex;
    align-items: center;
    white-space: nowrap;
    height: 24px;
  }
  .contact-item:nth-child(1) { top: 92px; }
  .contact-item:nth-child(2) { top: 124px; }
  .contact-item:nth-child(3) { top: 155px; }
  .contact-item:nth-child(4) { top: 187px; }
  .contact-icon {
    width: 24px;
    height: 24px;
    flex: none;
    margin-right: 5px;
  }
  .contact-icon .badge { fill: var(--brand-green); }
  .contact-icon .glyph { fill: var(--icon-white); }
  .contact-icon .glyph-line { fill: none; stroke: var(--brand-green); stroke-width: 0.9; }
</style>
</head>
<body>
<footer class="letterhead-footer">
  <svg class="decor-arcs" width="1200" height="241" viewBox="0 0 1200 241" aria-hidden="true">
    <circle cx="892" cy="383" r="330" fill="var(--arc-shade)" fill-opacity="0.058"/>
    <circle cx="700" cy="623" r="446" fill="var(--arc-shade)" fill-opacity="0.085"/>
    <circle cx="1164" cy="314" r="314" fill="var(--arc-shade)" fill-opacity="0.13"/>
  </svg>

  <ul class="contact-list">
    <li class="contact-item">
      <svg class="contact-icon" viewBox="0 0 24 24" aria-hidden="true">
        <circle class="badge" cx="12" cy="12" r="12"/>
        <path class="glyph" d="M12 4.5a5 5 0 0 0-5 5c0 3.6 5 9.5 5 9.5s5-5.9 5-9.5a5 5 0 0 0-5-5zm0 7a2 2 0 1 1 0-4 2 2 0 0 1 0 4z"/>
      </svg>
      <span class="contact-text">412 Fenwick Avenue #300 Dallas, TX 75319</span>
    </li>
    <li class="contact-item">
      <svg class="contact-icon" viewBox="0 0 24 24" aria-hidden="true">
        <circle class="badge" cx="12" cy="12" r="12"/>
        <path class="glyph" d="M8.2 5.5l2 2.6c.3.4.2 1-.1 1.3l-1 1c.8 1.6 2 2.9 3.6 3.7l1-1c.4-.3.9-.4 1.3-.1l2.6 1.9c.4.3.5.9.2 1.3l-1.1 1.4c-.5.6-1.3.8-2 .5-3.6-1.4-6.4-4.2-7.8-7.8-.3-.7-.1-1.5.5-2l1.4-1.1c.5-.3 1.1-.2 1.4.3z"/>
      </svg>
      <span class="contact-text">866-492-ACRE</span>
    </li>
    <li class="contact-item">
      <svg class="contact-icon" viewBox="0 0 24 24" aria-hidden="true">
        <circle class="badge" cx="12" cy="12" r="12"/>
        <rect class="glyph" x="5.5" y="6" width="13" height="12" rx="1"/>
        <path class="glyph-line" d="M5.5 8.5h13M8 11h8M8 13h8M8 15h8M7 11v5"/>
      </svg>
      <span class="contact-text">www.quillbrookacres.com</span>
    </li>
    <li class="contact-item">
      <svg class="contact-icon" viewBox="0 0 24 24" aria-hidden="true">
        <circle class="badge" cx="12" cy="12" r="12"/>
        <rect class="glyph" x="5" y="7.5" width="14" height="9.5"/>
        <path class="glyph-line" d="M5 7.5l7 5.5 7-5.5M5 17l5-4.5M19 17l-5-4.5"/>
      </svg>
      <span class="contact-text">info@quillbrookacres.com</span>
    </li>
  </ul>
</footer>
</body>
</html>
```